JT & WE Shearing Pty Ltd

We already have an existing logo created by Lumen Quarry however we have restructured to a company. We would like someone to add Pty Ltd to our business name please.

Colors

Designer to choose only greyscale colors for use in the design.

```html
<!DOCTYPE html>
<html lang="en">
<head>
<meta charset="utf-8">
<title>JT &amp; WE Shearing Pty Ltd — Business Card</title>
<link rel="stylesheet" href="https://fonts.googleapis.com/css2?family=Merriweather:wght@400;700;900&display=swap">
<style>
  :root {
    --page: #d9d9d9;
    --ink: #1c1c1c;
    --card-dark: #1f1f1f;
    --card-light: #ffffff;
    --text-light: #f4f4f4;
    --muted: #3a3a3a;
  }
  * { box-sizing: border-box; margin: 0; padding: 0; }
  html, body { width: 1200px; height: 880px; overflow: hidden; }
  body {
    background: var(--page);
    font-family: "Merriweather", Georgia, serif;
    color: var(--ink);
    display: flex;
    flex-direction: column;
    align-items: center;
    justify-content: center;
    gap: 40px;
  }
  .card {
    width: 680px;
    height: 388px;
    border-radius: 22px;
    position: relative;
    box-shadow: 0 6px 18px rgba(0,0,0,0.18);
  }
  .card--front {
    background: var(--card-dark);
    display: flex;
    align-items: center;
    justify-content: center;
  }
  .card--back { background: var(--card-light); }

  .wordmark {
    font-weight: 900;
    letter-spacing: 0.5px;
    white-space: nowrap;
  }
  .card--front .wordmark { color: var(--text-light); font-size: 38px; }
  .card--back .wordmark {
    position: absolute;
    right: 52px;
    top: 78px;
    color: var(--ink);
    font-size: 30px;
  }

  .rule { position: absolute; height: 2px; background: var(--ink); }
  .rule--company { left: 300px; right: 52px; top: 168px; }
  .rule--person { left: 200px; width: 170px; top: 266px; }

  .company {
    position: absolute;
    right: 52px;
    top: 184px;
    text-align: right;
    font-size: 13px;
    line-height: 1.6;
  }
  .company__name { font-weight: 700; }

  .person {
    position: absolute;
    left: 44px;
    top: 250px;
  }
  .person__name { font-weight: 900; font-size: 17px; letter-spacing: 0.5px; }
  .person__role { font-size: 13px; color: var(--muted); margin-top: 2px; }

  .contacts {
    position: absolute;
    left: 44px;
    top: 312px;
    list-style: none;
    font-size: 13px;
    line-height: 1.75;
  }
  .contacts li { display: flex; align-items: center; gap: 8px; }
  .contacts svg { width: 15px; height: 15px; flex: none; }
</style>
</head>
<body>
  <section class="card card--front" aria-label="Card front">
    <p class="wordmark">JT &amp; WE Shearing Pty Ltd</p>
  </section>

  <section class="card card--back" aria-label="Card back">
    <p class="wordmark">JT &amp; WE Shearing Pty Ltd</p>
    <div class="rule rule--company"></div>
    <div class="company">
      <p class="company__name">JT &amp; WE Shearing Pty Ltd</p>
      <p>PO Box 418 Ridgevale WA 6999</p>
    </div>

    <div class="person">
      <p class="person__name">CALLUM REID</p>
      <p class="person__role">President</p>
    </div>
    <div class="rule rule--person"></div>

    <ul class="contacts">
      <li>
        <svg viewBox="0 0 16 16" aria-hidden="true"><circle cx="8" cy="8" r="8" fill="#1c1c1c"/><rect x="5.5" y="3.5" width="5" height="9" rx="1" fill="none" stroke="#fff" stroke-width="1.2"/></svg>
        Tom 0400 555 182
      </li>
      <li>
        <svg viewBox="0 0 16 16" aria-hidden="true"><circle cx="8" cy="8" r="8" fill="#1c1c1c"/><rect x="4" y="5" width="8" height="6" fill="none" stroke="#fff" stroke-width="1.1"/><path d="M4 5 L8 8.5 L12 5" fill="none" stroke="#fff" stroke-width="1.1"/></svg>
        jtweshearing@mailbox.example
      </li>
    </ul>
  </section>
</body>
</html>
```